Homepage/Landing Page for Kelvadu.com

We need a brochure style landing page for our website, kelvadu.com. The new homepage will direct people either to trademarkhub.com (a website for businesses to purchase printing), to a landing page about trading cards/sports memorabilia, or to a website about high-end embellished cartons/boxes.
The existing site, www.kelvadu.com, will become trademarkhub.com, and people arriving at kelvadu.com will be shown three options to choose based on their needs:
1) Business Printing - for everyone from micro-businesses on up, our manufacturing process insures we have something to suit every business.
2) Highly decorated and embellished cartons - perfect for new brands, prototypes, pilot programs, seasonal packaging
3) Trading cards/sports memorabilia - Handling cards for athletes from Tidy Circuit to high school, college and beyond.

Target Market(s)

Target market is small business owners and print buyers

Industry/Entity Type

Printing and Packaging

Number of Pages Required

1 page

Font styles to use
Other font styles liked:
• See the KV Web Flip Standards PDF attached.

Requirements
Must have
• 3 clearly marked paths for customers to follow - use web standards pdf below for fonts and colors
Should not have
• My project should not feel trendy or faddish, but modern and professional.

```html
<!DOCTYPE html>
<html lang="en">
<head>
<meta charset="utf-8">
<title>Kelvadu — Positively Different Print</title>
<link href="https://fonts.googleapis.com/css2?family=Domine:wght@400;700&family=Work+Sans:wght@400;500&display=swap" rel="stylesheet">
<style>
:root{
  --teal:#00a9c9;
  --teal-dark:#0092ae;
  --ink:#111111;
  --body:#3a3a3a;
  --muted:#b8b8b8;
  --mist:#f6fbfc;
  --white:#ffffff;
  --night:#0b0b0b;
}
*{box-sizing:border-box;margin:0;padding:0}
html,body{width:1200px;height:2515px;overflow:hidden}
body{font-family:"Work Sans",Arial,sans-serif;color:var(--body);background:var(--white);position:relative}
.serif{font-family:"Domine",Georgia,serif}
a{color:inherit;text-decoration:none}

.site-header{position:absolute;top:0;left:0;width:1200px;height:90px;background:var(--white)}
.brand{position:absolute;left:161px;top:31px;display:flex;align-items:center;gap:8px;font-family:"Domine",Georgia,serif;font-size:22px;font-weight:700;color:var(--teal)}
.brand-mark{width:14px;height:14px;background:var(--teal)}
.main-nav{position:absolute;left:535px;top:37px;display:flex;gap:41px;font-family:"Domine",Georgia,serif;font-size:13px;color:var(--ink);letter-spacing:.3px}
.nav-tools{position:absolute;left:941px;top:33px;display:flex;gap:12px;align-items:center;padding-left:18px;border-left:1px solid #ddd;height:22px}

.hero{position:absolute;top:90px;left:0;width:1200px;height:529px;background:linear-gradient(90deg,#4a4a4a 0%,#6b6560 35%,#8a8a92 55%,#5a6a8a 75%,#b7b5b2 100%)}
.hero-copy{position:absolute;left:164px;top:150px;width:400px;color:var(--white)}
.hero-title{font-size:36px;line-height:50px;font-weight:400}
.hero-title .mark{box-shadow:inset 0 -6px 0 var(--teal)}
.hero-text{margin-top:10px;font-size:15px;line-height:22.5px}
.btn{display:inline-flex;align-items:center;gap:8px;background:var(--teal);color:var(--white);font-size:14px;font-weight:500;letter-spacing:.6px;text-transform:uppercase}
.hero .btn{position:absolute;left:161px;top:365px;height:45px;padding:0 15px}
.scroll-cue{position:absolute;left:577px;top:577px;width:46px;height:46px;background:var(--white);transform:rotate(45deg);box-shadow:0 4px 10px rgba(0,0,0,.08)}
.scroll-cue svg{position:absolute;left:11px;top:11px;transform:rotate(-45deg)}

.needs-title{position:absolute;top:712px;width:1200px;text-align:center;font-size:36px;color:var(--ink)}
.needs-icon{position:absolute;left:589px;top:678px}
.path-card{position:absolute;top:789px;width:278px;height:315px;background:var(--white);box-shadow:0 2px 12px rgba(0,0,0,.07);text-align:center;overflow:hidden}
.path-card .halo{position:absolute;left:89px;top:-50px;width:100px;height:100px;background:var(--mist);transform:rotate(45deg)}
.path-card svg.icon{position:relative;margin-top:36px}
.path-card h3{margin-top:36px;font-family:"Domine",Georgia,serif;font-size:16px;line-height:24px;font-weight:400;color:var(--ink);letter-spacing:.4px;text-transform:uppercase}
.path-card p{margin:8px auto 0;width:250px;font-size:13.3px;line-height:19.5px}
.path-card .open{position:absolute;left:99px;bottom:-6px}

.proof-band{position:absolute;top:1186px;left:0;width:1200px;height:386px;background:var(--mist)}
.feature-card{position:absolute;top:74px;width:420px;height:236px;background:var(--white);text-align:center}
.feature-name{margin-top:46px;height:50px;font-size:38px;color:var(--teal);font-weight:400}
.feature-card p{margin-top:32px;font-size:13.3px;line-height:19.5px}
.feature-card .btn{position:absolute;left:0;bottom:0;width:420px;height:37px;justify-content:center}

.tagline{position:absolute;top:1640px;width:1200px;text-align:center;color:var(--ink)}
.tagline .line{font-size:35px;line-height:59px}
.tagline .accent{color:var(--teal);font-weight:700;letter-spacing:13px;font-size:35px;line-height:59px}

.community{position:absolute;top:1873px;left:0;width:1200px;height:307px;background:var(--night);text-align:center;color:var(--white)}
.rays{position:absolute;top:0;width:240px;height:307px}
.rays.left{left:0;background:linear-gradient(90deg,#c5a800 0%,#1f6e8c 30%,#a0126a 60%,rgba(11,11,11,0) 100%)}
.rays.right{right:0;background:linear-gradient(270deg,#c5a800 0%,#1f6e8c 30%,#a0126a 60%,rgba(11,11,11,0) 100%)}
.community h2{position:relative;margin-top:68px;font-size:35px;font-weight:400}
.community p{position:relative;margin-top:14px;font-size:17px;letter-spacing:.3px}
.community .btn{position:relative;margin-top:24px;height:45px;padding:0 15px}

.site-footer{position:absolute;top:2180px;left:0;width:1200px;height:335px;background:var(--teal);color:var(--white)}
.footer-brand{position:absolute;left:161px;top:98px;display:flex;align-items:center;gap:10px;font-family:"Domine",Georgia,serif;font-size:26px;font-weight:700}
.footer-brand .brand-mark{background:var(--white)}
.motto{position:absolute;left:248px;top:124px;font-size:20px;line-height:32px;letter-spacing:1.5px}
.footer-col{position:absolute;top:76px}
.footer-col h4{font-family:"Domine",Georgia,serif;font-weight:400;font-size:18px;letter-spacing:.5px;margin-bottom:17px}
.footer-col li{list-style:none;font-size:13px;line-height:27px;padding-left:2px}
.contact-row{display:flex;gap:8px;font-size:13px;line-height:17px;margin-bottom:13px}
.contact-row svg{flex:none;margin-top:2px}
.footer-rule{position:absolute;left:161px;top:273px;width:878px;height:1px;background:rgba(255,255,255,.45)}
.copyright{position:absolute;top:295px;width:1200px;text-align:center;font-size:13px}
</style>
</head>
<body>

<header class="site-header">
  <a class="brand" href="#"><span class="brand-mark"></span>Kelvadu</a>
  <nav class="main-nav"><a href="#">Products</a><a href="#">Services</a><a href="#">About Us</a><a href="#">Contact Us</a></nav>
  <div class="nav-tools">
    <svg width="14" height="14" viewBox="0 0 14 14" fill="none" stroke="#333" stroke-width="1.2"><circle cx="6" cy="6" r="4.5"/><path d="M9.5 9.5L13 13"/></svg>
    <svg width="14" height="15" viewBox="0 0 14 15" fill="none" stroke="#333" stroke-width="1.2"><circle cx="7" cy="4.5" r="3.5"/><path d="M1 14.5c0-3.5 2.7-6 6-6s6 2.5 6 6"/></svg>
    <svg width="16" height="17" viewBox="0 0 16 17" fill="none" stroke="#333" stroke-width="1.2"><path d="M2 5h9v10H2z"/><path d="M4 5V3.5a2.5 2.5 0 015 0V5"/><circle cx="13" cy="14" r="2.6" fill="#00a9c9" stroke="none"/></svg>
  </div>
</header>

<section class="hero">
  <div role="img" aria-label="Photo of a print team reviewing proofs together in a bright studio" style="position:absolute;inset:0"></div>
  <div style="position:absolute;inset:0;background:linear-gradient(90deg,rgba(20,20,20,.55) 0%,rgba(20,20,20,.3) 45%,rgba(20,20,20,0) 60%)"></div>
  <div class="hero-copy">
    <h1 class="hero-title serif">We’re A Different Kind Of <span class="mark">Printer.</span></h1>
    <p class="hero-text">Kelvadu works directly with creatives and creatives only. Our network of creatives brings the inspiration, we provide the tools and the expertise to turn visions into reality.</p>
  </div>
  <a class="btn" href="#">Contact Us
    <svg width="16" height="10" viewBox="0 0 16 10" fill="none" stroke="#fff" stroke-width="1.2"><path d="M0 5h15M10.5 .5L15 5l-4.5 4.5"/></svg></a>
</section>
<div class="scroll-cue"><svg width="24" height="24" viewBox="0 0 24 24" fill="none" stroke="#00a9c9" stroke-width="1.2"><path d="M12 3v17M6.5 14.5L12 20l5.5-5.5"/></svg></div>

<svg class="needs-icon" width="22" height="22" viewBox="0 0 22 22"><rect x="4" y="4" width="14" height="14" fill="#00a9c9"/></svg>
<h2 class="needs-title serif">What You Need</h2>

<article class="path-card" style="left:161px">
  <div class="halo"></div>
  <svg class="icon" width="62" height="76" viewBox="0 0 62 76" fill="none" stroke="#00a9c9" stroke-width="2"><rect x="14" y="2" width="34" height="30"/><path d="M20 10h22M20 16h22M20 22h16"/><rect x="2" y="32" width="58" height="28" rx="3"/><rect x="10" y="52" width="42" height="20"/><circle cx="52" cy="40" r="2"/></svg>
  <h3>Business Printing</h3>
  <p>for everyone from micro-businesses on up, our manufacturing process insures we have something to suit every business.</p>
  <svg class="open" width="80" height="46" viewBox="0 0 80 46"><path d="M40 0L80 46H0z" fill="#00a9c9"/><path d="M40 20v16M32 28h16" stroke="#fff" stroke-width="1.6"/></svg>
</article>

<article class="path-card" style="left:461px">
  <div class="halo"></div>
  <svg class="icon" width="78" height="76" viewBox="0 0 78 76" fill="none" stroke="#00a9c9" stroke-width="2"><path d="M2 20l8-16h16l8 16v54H2z"/><path d="M2 20h32M8 36h18M8 44h18"/><path d="M36 28l6-12h22l6 12v46H36z"/><path d="M36 28h34M46 42h12v18H46z"/></svg>
  <h3>Highly Decorated and Embellished Cartons</h3>
  <p>perfect for new brands, prototypes, pilot programs, seasonal packaging</p>
  <svg class="open" width="80" height="46" viewBox="0 0 80 46"><path d="M40 0L80 46H0z" fill="#c9c9c9"/><path d="M40 20v16M32 28h16" stroke="#fff" stroke-width="1.6"/></svg>
</article>

<article class="path-card" style="left:761px">
  <div class="halo"></div>
  <svg class="icon" width="62" height="76" viewBox="0 0 62 76" fill="none" stroke="#00a9c9" stroke-width="2"><rect x="2" y="2" width="48" height="66" rx="4"/><rect x="8" y="6" width="48" height="66" rx="4"/><rect x="13" y="10" width="48" height="64" rx="4" fill="#fff"/><rect x="19" y="17" width="36" height="48" rx="2"/><path d="M37 28l10 6v12l-10 6-10-6V34z"/></svg>
  <h3>Trading Cards/<br>Sports Memorabilia</h3>
  <p>Handling cards for athletes from Tidy Circuit to high school, college and beyond.</p>
  <svg class="open" width="80" height="46" viewBox="0 0 80 46"><path d="M40 0L80 46H0z" fill="#c9c9c9"/><path d="M40 20v16M32 28h16" stroke="#fff" stroke-width="1.6"/></svg>
</article>

<section class="proof-band">
  <article class="feature-card" style="left:161px">
    <div class="feature-name serif">Sure Sample</div>
    <p>An actual finished sample. See it. Touch it.<br>Feel it. Before you print.</p>
    <a class="btn" href="#">Learn More <svg width="16" height="10" viewBox="0 0 16 10" fill="none" stroke="#fff" stroke-width="1.2"><path d="M0 5h15M10.5 .5L15 5l-4.5 4.5"/></svg></a>
  </article>
  <article class="feature-card" style="left:619px">
    <div class="feature-name serif">TrueTone</div>
    <p>95% of the Chromaguide library without the hassle,<br>cost or delay of special mixes.</p>
    <a class="btn" href="#">Learn More <svg width="16" height="10" viewBox="0 0 16 10" fill="none" stroke="#fff" stroke-width="1.2"><path d="M0 5h15M10.5 .5L15 5l-4.5 4.5"/></svg></a>
  </article>
</section>

<section class="tagline serif">
  <div class="line">Surprisingly Different Print</div>
  <div class="accent">EXCLUSIVELY</div>
  <div class="line">For The Creative Industry</div>
</section>

<section class="community">
  <div class="rays left" role="img" aria-label="Decorative bursts of yellow, blue and magenta light rays"></div>
  <div class="rays right" role="img" aria-label="Decorative bursts of yellow, blue and magenta light rays"></div>
  <h2 class="serif">Grow The Community. Get Great Stuff.</h2>
  <p>Share us with your colleagues for exclusive tools and resources.</p>
  <a class="btn" href="#">Contact Us <svg width="16" height="10" viewBox="0 0 16 10" fill="none" stroke="#fff" stroke-width="1.2"><path d="M0 5h15M10.5 .5L15 5l-4.5 4.5"/></svg></a>
</section>

<footer class="site-footer">
  <div class="footer-brand"><span class="brand-mark"></span>Kelvadu</div>
  <div class="motto serif" style="top:118px;left:248px;display:none"></div>
  <div class="motto serif" style="left:161px;top:150px">POSITIVELY<br>DIFFERENT.</div>
  <div class="footer-col" style="left:459px"><h4>Expect More</h4><ul><li>All Products</li><li>TrueTone™</li><li>Sure Sample™</li><li>Turnaround</li></ul></div>
  <div class="footer-col" style="left:638px"><h4>About Us</h4><ul><li>Creatives Only</li><li>Terms of Service</li><li>Privacy Policy</li><li>FAQ</li><li style="font-weight:500">Refer a Colleague</li></ul></div>
  <div class="footer-col" style="left:809px"><h4>Contact Us</h4>
    <div class="contact-row"><svg width="12" height="16" viewBox="0 0 12 16" fill="#fff"><path d="M6 0a6 6 0 00-6 6c0 4.5 6 10 6 10s6-5.5 6-10a6 6 0 00-6-6zm0 8.5A2.5 2.5 0 116 3.5a2.5 2.5 0 010 5z"/></svg><span>Kelvadu<br>4410 Harbor Mill Road<br>Lindenvale, TX 75990</span></div>
    <div class="contact-row"><svg width="14" height="14" viewBox="0 0 14 14" fill="#fff"><path d="M3 0l2.5 3.5-1.5 2a8 8 0 004.5 4.5l2-1.5L14 11l-2 3C5 14 0 9 0 2z"/></svg><span>855.Go.Kelvadu (855.465.3582)</span></div>
    <div class="contact-row"><svg width="14" height="11" viewBox="0 0 14 11" fill="#fff"><path d="M0 0h14v1.5L7 6 0 1.5zM0 3l7 4.5L14 3v8H0z"/></svg><span>support@kelvadu.com</span></div>
  </div>
  <div class="footer-rule"></div>
  <div class="copyright">Copyright 2022 Kelvadu.com. All Rights Reserved.</div>
</footer>

</body>
</html>
```